CEDAR KEEP LOCKERS

Please see the attached. I need a new postcard design with a soccer theme with the headline "Score Big at Cedar Keep Lockers and make it your goal to Store Your Stuff." Everything else that is on the current card stays the same on this new card design, copy, address, phone, etc.

```html
<!DOCTYPE html>
<html lang="en">
<head>
<meta charset="utf-8">
<title>Cedar Keep Lockers – Soccer Postcard</title>
<link href="https://fonts.googleapis.com/css2?family=Titan+One&family=Oswald:wght@500;700&family=Open+Sans:wght@700;800&display=swap" rel="stylesheet">
<style>
  :root{
    --page:#eceff1;
    --crimson:#d0103f;
    --yellow:#fff200;
    --gold:#f4c400;
    --ink:#111111;
    --white:#ffffff;
    --grass-dark:#2f6d1c;
    --grass-light:#5aa52e;
    --sky:#8fd3ef;
    --lime:#c8e84a;
    --frame-green:#1f8a5a;
  }
  *{box-sizing:border-box;margin:0;padding:0}
  html,body{width:816px;height:1200px;overflow:hidden;background:var(--page)}
  .canvas{position:relative;width:816px;height:1200px}
  .card{position:absolute;left:40px;width:736px;height:545px;overflow:hidden;box-shadow:0 4px 14px rgba(0,0,0,.25)}

  /* ---------- front ---------- */
  .card--front{top:30px;background:radial-gradient(ellipse at 50% 45%,var(--grass-light),var(--grass-dark))}
  .front__headline{position:absolute;top:14px;left:0;right:0;text-align:center;font-family:"Titan One",sans-serif;font-size:84px;line-height:1;color:var(--yellow);text-shadow:3px 3px 0 var(--ink)}
  .front__headline .accent{color:var(--crimson);text-shadow:3px 3px 0 var(--white)}
  .front__ball{position:absolute;left:52px;top:160px;width:308px;height:308px;border-radius:50%;background:radial-gradient(circle at 40% 35%,#ffffff,#c9ccce 70%,#8d9194)}
  .front__brand{position:absolute;left:452px;top:170px;width:210px;display:flex;align-items:flex-start;gap:12px}
  .brand__square{flex:none;width:22px;height:22px;background:var(--yellow);margin-top:14px}
  .brand__name{font-family:"Oswald",sans-serif;font-weight:700;font-size:50px;line-height:1.05;color:var(--yellow)}
  .front__tagline{position:absolute;right:34px;top:392px;text-align:right;font-family:"Titan One",sans-serif;color:var(--white);text-shadow:2px 2px 0 var(--ink)}
  .tagline__small{font-size:34px;line-height:1.1}
  .tagline__mid{font-size:48px;line-height:1.1}
  .tagline__big{font-size:56px;line-height:1.1;color:var(--yellow)}
  .tagline .red,.front__tagline .red{color:var(--crimson);text-shadow:2px 2px 0 var(--white)}

  /* ---------- back ---------- */
  .card--back{top:625px;background:linear-gradient(160deg,var(--sky) 0%,#b9e6d0 45%,var(--lime) 80%,#8fcf3a 100%)}
  .back__ball{position:absolute;left:10px;top:-12px;width:250px;height:250px;border-radius:50%;background:radial-gradient(circle at 45% 40%,#ffffff,#dfe6e3 65%,#1d5a3e 100%)}
  .back__brand{position:absolute;left:72px;top:54px;display:flex;gap:10px;align-items:flex-start}
  .back__brand .brand__square{width:16px;height:16px;margin-top:10px;background:var(--crimson)}
  .back__brand .brand__name{font-size:34px;color:var(--crimson)}
  .contact{position:absolute;left:36px;top:262px;width:204px;height:194px;background:var(--yellow);border:3px solid var(--frame-green);text-align:center;font-family:"Oswald",sans-serif}
  .contact__cta{margin-top:10px;font-weight:700;font-size:20px;line-height:1;color:var(--crimson)}
  .contact__sub{font-weight:500;font-size:14px;color:var(--crimson);margin-top:2px}
  .contact__phone{margin:8px -8px 0;background:var(--crimson);color:var(--white);font-weight:700;font-size:25px;padding:2px 0}
  .contact__address{margin-top:10px;font-family:"Open Sans",sans-serif;font-weight:700;font-size:13.5px;line-height:1.35;color:var(--ink)}
  .contact__web{position:absolute;left:-10px;right:-10px;bottom:18px;background:var(--crimson);color:var(--white);font-family:"Open Sans",sans-serif;font-weight:800;font-size:11.5px;padding:3px 0}
  .offer{position:absolute;right:36px;top:46px;width:400px;text-align:right}
  .offer__lead{font-family:"Open Sans",sans-serif;font-weight:800;font-size:40px;line-height:1;color:var(--ink);letter-spacing:1px}
  .offer__name{font-family:"Oswald",sans-serif;font-weight:700;font-size:36px;line-height:1.1;color:var(--crimson)}
  .offer__today{text-align:center;padding-left:70px;font-family:"Titan One",sans-serif;font-size:62px;line-height:1;color:var(--yellow);text-shadow:2px 2px 0 var(--ink),-1px -1px 0 var(--ink)}
  .features{list-style:none;margin-top:26px;font-family:"Open Sans",sans-serif;font-weight:700;font-size:14.5px;line-height:1.65;color:var(--ink)}
  .features .hl{color:var(--crimson)}
  .features .price{font-family:"Oswald",sans-serif;font-weight:700;font-size:18px;color:var(--crimson)}
  .features .was{color:var(--crimson);text-decoration:line-through;text-decoration-color:var(--gold);text-decoration-thickness:2px}
  .features .gap{margin-top:6px}
  .banner{position:absolute;left:0;right:0;bottom:0;height:56px;background:rgba(210,235,90,.85);text-align:center;font-family:"Titan One",sans-serif;font-size:29px;line-height:56px;color:var(--crimson)}
</style>
</head>
<body>
<main class="canvas">

  <section class="card card--front" aria-label="Postcard front">
    <h1 class="front__headline">SCORE <span class="accent">BIG</span> AT</h1>
    <div class="front__ball" role="img" aria-label="Soccer ball resting on grass"></div>
    <div class="front__brand">
      <span class="brand__square"></span>
      <span class="brand__name">Cedar Keep Lockers</span>
    </div>
    <p class="front__tagline">
      <span class="tagline__small">and Make It Your</span><br>
      <span class="tagline__mid"><span class="red">GOAL</span> TO</span><br>
      <span class="tagline__big"><span class="red">STORE</span> YOUR STUFF.</span>
    </p>
  </section>

  <section class="card card--back" aria-label="Postcard back">
    <div class="back__ball" role="img" aria-label="Illustrated soccer ball"></div>
    <div class="back__brand">
      <span class="brand__square"></span>
      <span class="brand__name">Cedar Keep<br>Lockers</span>
    </div>

    <div class="contact">
      <p class="contact__cta">CALL TODAY FOR</p>
      <p class="contact__sub">LIMITED TIME SAVINGS!</p>
      <p class="contact__phone">(555) 014-2290</p>
      <p class="contact__address">1840 ALDER RD<br>FAIRVIEW, IN 46001</p>
      <p class="contact__web">WWW.CEDARKEEPLOCKERS.COM</p>
    </div>

    <div class="offer">
      <h2 class="offer__lead">SAVE BIG WITH</h2>
      <p class="offer__name">CEDAR KEEP LOCKERS</p>
      <p class="offer__today">TODAY</p>
      <ul class="features">
        <li><span class="price">5X5</span> STANDARD-WAS <span class="was">$54</span> NOW <span class="price">$47</span></li>
        <li><span class="price">10X10</span> STANDARD- WAS <span class="was">$165</span> NOW <span class="price">$149</span></li>
        <li class="gap">CUSTOMIZED <span class="hl">LEASE &amp; PAYMENT</span> OPTIONS -<br>PACKING, MOVING &amp; STORAGE SUPPLIES</li>
        <li class="gap"><span class="hl">24 HOUR</span> CODED GATE ACCESS -<br>MOTION SENSOR PROPERTY LIGHTS</li>
        <li>SOPHISTICATED <span class="hl">SURVEILLANCE</span> -<br>DAILY PROPERTY INSPECTIONS</li>
      </ul>
    </div>

    <p class="banner">WE SELL LOCKS, BOXES &amp; PACKING SUPPLIES!</p>
  </section>

</main>
</body>
</html>
```